Create a jpg / pdf for a design for rear car window stickers

I am looking to create some rear car window stickers which measure 300mm x 50mm. I would like the sticker to just say FLARE Cars on the green background with dark silver text to stand out. with the web address below smaller. www.flaringofcars.co.uk. Kind regards, DAniel

I attach our current sticker but we are looking to have more impact with less on there.

I MUST STRESS, WE MUST USE THE SAME LOGO AND GREEN .

```html
<!DOCTYPE html>
<html lang="en">
<head>
<meta charset="utf-8">
<title>FLARE Cars – rear window sticker options</title>
<link rel="stylesheet" href="https://fonts.googleapis.com/css2?family=Marcellus&family=Playfair+Display:ital,wght@1,900&family=Titan+One&family=Fondamento:ital@1&family=Berkshire+Swash&family=Ultra&family=Didact+Gothic&display=swap">
<style>
  :root {
    --sticker-green: #36ad49;
    --frame-white: #ffffff;
    --page-white: #ffffff;
    --silver-light: #ffffff;
    --silver-mid: #d6d6d6;
    --silver-dark: #8f8f8f;
  }
  * { margin: 0; padding: 0; box-sizing: border-box; }
  html, body {
    width: 900px;
    height: 1200px;
    overflow: hidden;
    background: var(--page-white);
  }
  .sheet {
    position: relative;
    width: 900px;
    height: 1200px;
  }
  .sticker {
    position: absolute;
    left: 0;
    width: 900px;
    height: 148px;
    background: var(--sticker-green);
  }
  .sticker::before {
    content: "";
    position: absolute;
    inset: 9px 8px 9px 8px;
    border: 1.5px solid var(--frame-white);
  }
  .sticker--1 { top: 40px; }
  .sticker--2 { top: 238px; }
  .sticker--3 { top: 426px; }
  .sticker--4 { top: 613px; }
  .sticker--5 { top: 800px; }
  .sticker--6 { top: 994px; }

  .sticker__name {
    position: absolute;
    left: 0;
    right: 0;
    top: 14px;
    text-align: center;
    line-height: 1;
    white-space: nowrap;
    color: transparent;
    background: linear-gradient(180deg, var(--silver-mid) 0%, var(--silver-light) 40%, var(--silver-mid) 65%, var(--silver-dark) 100%);
    -webkit-background-clip: text;
    background-clip: text;
  }
  .sticker__web {
    position: absolute;
    left: 185px;
    top: 102px;
    font-family: "Didact Gothic", sans-serif;
    font-size: 35px;
    line-height: 1;
    letter-spacing: 0.2px;
    color: var(--frame-white);
    white-space: nowrap;
  }

  .name--classic   { font-family: "Marcellus", serif; font-size: 64px; top: 16px; padding-left: 4px; }
  .name--italic    { font-family: "Playfair Display", serif; font-style: italic; font-weight: 900; font-size: 66px; top: 14px; padding-left: 40px; }
  .name--heavy     { font-family: "Titan One", sans-serif; font-size: 62px; top: 20px; }
  .name--calligraph{ font-family: "Fondamento", cursive; font-style: italic; font-size: 72px; top: 8px; padding-left: 50px; }
  .name--script    { font-family: "Berkshire Swash", cursive; font-size: 66px; top: 16px; }
  .name--slab      { font-family: "Ultra", serif; font-size: 60px; top: 20px; padding-left: 40px; }
</style>
</head>
<body>
  <main class="sheet">
    <section class="sticker sticker--1">
      <h1 class="sticker__name name--classic">FLARE Cars</h1>
      <p class="sticker__web">WWW.FLARINGOFCARS.CO.UK</p>
    </section>
    <section class="sticker sticker--2">
      <h1 class="sticker__name name--italic">FLARE Cars</h1>
      <p class="sticker__web">WWW.FLARINGOFCARS.CO.UK</p>
    </section>
    <section class="sticker sticker--3">
      <h1 class="sticker__name name--heavy">FLARE Cars</h1>
      <p class="sticker__web">WWW.FLARINGOFCARS.CO.UK</p>
    </section>
    <section class="sticker sticker--4">
      <h1 class="sticker__name name--calligraph">FLARE Cars</h1>
      <p class="sticker__web">WWW.FLARINGOFCARS.CO.UK</p>
    </section>
    <section class="sticker sticker--5">
      <h1 class="sticker__name name--script">Flare Cars</h1>
      <p class="sticker__web">WWW.FLARINGOFCARS.CO.UK</p>
    </section>
    <section class="sticker sticker--6">
      <h1 class="sticker__name name--slab">FLARE Cars</h1>
      <p class="sticker__web">WWW.FLARINGOFCARS.CO.UK</p>
    </section>
  </main>
</body>
</html>
```